Inspiring Poster for Company Staff Room

What we need:
We want an awesome design to create a poster that will be plaque mounted in our staff room. We just went through a very motivating workshop to discover our "WHY" as a company...basically, to define the reason we are in business, and to define what motivates us to come to work every day. The poster must be motivating but really resonate with our team…we are not looking for a “typical” motivational poster that we can purchase off Amazon!

Who we are:
We are a property management company, a team of 20 that is passionate about our investors, and residents who rent from us, but more importantly, we love helping people and making a difference in our industry. We are proud and work hard for every single 5 star Google review we achieve.

Information for you:
We have included a mock up of the poster, which words we want, and the placement of them (in a general sense) but we need a designer to really bring this together in an inspiring poster that represents our company’s culture, feel, and fit. We have also included a logo file, as well as examples of our business cards, letterhead and thank you card already designed.
Here are the parameters:

(1) Poster size: 24” x 36”
(2) Full colour
(3) Must incorporate our company logo
(4) Must incorporate the following words:

Why do I come to work?

“To feel fulfilled by empathizing, educating and empowering our clients and co-workers so that we can build strong, impactful relationships”

Own the outcome

(5) Please see our website at www.brindlecovepm.com to get a feel for our company culture and for a better idea of our current company graphics

Target Market(s)

Our staff. Will not be seen by our clients

Industry/Entity Type

Real Estate

Font styles to use
Serif
Sans Serif

Requirements
Should not have
• Would not want this to be too "busy." if you can picture it, the poster will be mounted on the wall as soon as someone enters the room. The idea is to remind them each day why they come to work.

```html
<!DOCTYPE html>
<html lang="en">
<head>
<meta charset="utf-8">
<title>Why do I come to work? – Brindle Cove Property Management</title>
<link rel="stylesheet" href="https://fonts.googleapis.com/css2?family=Carlito:ital,wght@0,400;0,700;1,700&display=swap">
<style>
  :root {
    --poster-blue: #105a93;
    --frame-blue: #2a86c8;
    --mark-deep: #13406b;
    --mark-edge: #1c70b4;
    --text-pale: #dcecdf;
    --brand-blue: #2b9ad9;
  }
  * { margin: 0; padding: 0; box-sizing: border-box; }
  html, body {
    width: 1200px;
    height: 800px;
    overflow: hidden;
    background: var(--poster-blue);
  }
  .poster {
    position: relative;
    width: 1200px;
    height: 800px;
    background: var(--poster-blue);
    font-family: "Carlito", "Calibri", sans-serif;
    color: var(--text-pale);
    overflow: hidden;
  }
  .poster-frame {
    position: absolute;
    inset: 3px;
    border: 2px solid var(--frame-blue);
    pointer-events: none;
  }
  .question-mark {
    position: absolute;
    right: 30px;
    top: -60px;
    font-size: 600px;
    font-weight: 700;
    line-height: 1;
    color: var(--mark-deep);
    text-shadow: 10px 8px 0 var(--mark-edge);
    user-select: none;
  }
  .brand {
    position: absolute;
    left: 30px;
    top: 26px;
    display: flex;
    align-items: center;
    gap: 22px;
  }
  .brand-square {
    width: 86px;
    height: 86px;
    background: var(--brand-blue);
  }
  .brand-name {
    font-weight: 700;
    color: var(--brand-blue);
    text-transform: uppercase;
    line-height: 1;
  }
  .brand-name .brand-main {
    display: block;
    font-size: 66px;
    letter-spacing: 6px;
  }
  .brand-name .brand-sub {
    display: block;
    font-size: 26px;
    letter-spacing: 11px;
    margin-top: 6px;
  }
  .message {
    position: absolute;
    left: 0;
    right: 0;
    text-align: center;
  }
  .headline {
    top: 180px;
    font-size: 60px;
    font-weight: 700;
  }
  .why-statement {
    top: 328px;
    font-style: italic;
    font-weight: 700;
    line-height: 1;
  }
  .why-statement span { display: block; }
  .why-statement .small { font-size: 34px; }
  .why-statement .large { font-size: 46px; }
  .line-1 { margin-bottom: 24px; }
  .line-2 { margin-bottom: 22px; }
  .line-3 { margin-bottom: 16px; }
  .line-4 { margin-bottom: 18px; }
  .call-to-action {
    top: 692px;
    font-size: 50px;
    font-weight: 700;
    text-decoration: underline;
    text-decoration-thickness: 3px;
    text-underline-offset: 6px;
  }
</style>
</head>
<body>
  <main class="poster">
    <div class="question-mark" aria-hidden="true">?</div>

    <header class="brand">
      <div class="brand-square" aria-hidden="true"></div>
      <p class="brand-name">
        <span class="brand-main">Brindle Cove</span>
        <span class="brand-sub">Property Management</span>
      </p>
    </header>

    <h1 class="message headline">Why do I come to work?</h1>

    <blockquote class="message why-statement">
      <span class="small line-1">„To feel fulfilled by</span>
      <span class="large line-2">empathizing, educating and empowering</span>
      <span class="large line-3">our clients and co-workers</span>
      <span class="small line-4">so that</span>
      <span class="large">we can build strong, impactful relationships”</span>
    </blockquote>

    <p class="message call-to-action">Own the Outcome!</p>

    <div class="poster-frame" aria-hidden="true"></div>
  </main>
</body>
</html>
```